Need Business Cards, Letterhead, and Stationary

Hi, please design a full stationary set for the attached logo (Business Cards, Letterhead, A4 Envelope, and other important stationary items that you can think of)
Please be as creative as you wish. The logo is for An Founders Academy that teaches young and starting Entrepreneur skills they need to start their business.

```html
<!DOCTYPE html>
<html lang="en">
<head>
<meta charset="utf-8">
<title>Kernel Founders Academy – Stationery Set</title>
<link rel="stylesheet" href="https://fonts.googleapis.com/css2?family=Montserrat:wght@600;700&family=Open+Sans:ital,wght@0,400;0,600;1,400&display=swap">
<style>
:root{
  --yellow:#f6c515;
  --blue:#2e97d6;
  --charcoal:#3c3c3f;
  --grey:#8b8b8e;
  --paper:#ffffff;
  --ink:#5c5c60;
  --bg:#f0f0f1;
}
*{box-sizing:border-box;margin:0;padding:0}
html,body{width:1200px;height:1000px;overflow:hidden;background:var(--bg)}
body{font-family:"Open Sans",Arial,sans-serif;color:var(--ink)}
.canvas{position:relative;width:1200px;height:1000px;overflow:hidden;background:var(--bg)}
.item{position:absolute;background:var(--paper);box-shadow:0 2px 6px rgba(0,0,0,.12);overflow:hidden}
.item > svg.art{position:absolute;inset:0;width:100%;height:100%}

/* wordmark */
.mark{position:absolute;display:flex;align-items:center;gap:4px;font-family:"Montserrat",Arial,sans-serif;font-weight:700;color:var(--charcoal);letter-spacing:.5px;white-space:nowrap}
.mark .dot{display:inline-block;border-radius:50%;background:var(--yellow)}
.mark.xs{font-size:8px}.mark.xs .dot{width:7px;height:7px}
.mark.sm{font-size:11px}.mark.sm .dot{width:9px;height:9px}
.mark.lg{font-size:26px;gap:8px}.mark.lg .dot{width:22px;height:22px}

/* letter text */
.fine{position:absolute;font-size:4.2px;line-height:6px;color:var(--ink)}
.fine p{margin-bottom:5px}
.fine .to{color:var(--blue);font-weight:600}
.contact{position:absolute;font-size:3.6px;line-height:5px;color:var(--grey)}
.sign{position:absolute;font-size:4.2px;line-height:6px;text-align:right}
.sign em{display:block;font-size:8px;color:var(--charcoal)}

/* pens */
.pen{position:absolute;border-radius:6px;box-shadow:0 2px 4px rgba(0,0,0,.15)}
.pen .tip{position:absolute;left:50%;transform:translateX(-50%);border-radius:3px}
.pen .label{position:absolute;left:50%;top:50%;transform:translate(-50%,-50%) rotate(-90deg);font-family:"Montserrat",Arial,sans-serif;font-weight:700;font-size:8px;color:var(--charcoal)}

.badge{position:absolute;width:34px;height:34px;border-radius:50%;box-shadow:0 2px 4px rgba(0,0,0,.15);display:flex;align-items:center;justify-content:center}
.badge span{width:10px;height:10px;border-radius:50%;background:var(--paper)}

.card-name{position:absolute;font-family:"Montserrat",Arial,sans-serif;font-weight:700;font-size:6px;color:var(--paper)}
.card-role{position:absolute;font-size:3.6px;color:var(--paper)}
</style>
</head>
<body>
<main class="canvas">

  <!-- Folder front -->
  <section class="item folder-front" style="left:40px;top:35px;width:295px;height:335px">
    <svg class="art" viewBox="0 0 295 335" aria-hidden="true">
      <path d="M0 250 C70 245 130 285 165 335 L120 335 C90 300 45 282 0 282Z" fill="var(--yellow)"/>
      <path d="M0 335 L0 295 A40 40 0 0 1 40 335Z" fill="var(--yellow)"/>
      <path d="M295 250 C225 255 195 300 180 335 L225 335 C240 302 265 285 295 282Z" fill="var(--blue)"/>
      <path d="M295 335 L295 295 A40 40 0 0 0 255 335Z" fill="var(--blue)"/>
    </svg>
    <div class="mark xs" style="right:10px;top:8px"><span class="dot"></span>KERNEL</div>
  </section>

  <!-- Folder cover -->
  <section class="item folder-cover" style="left:385px;top:38px;width:240px;height:330px">
    <svg class="art" viewBox="0 0 240 330" aria-hidden="true">
      <rect x="0" y="0" width="170" height="150" fill="var(--yellow)"/>
      <rect x="110" y="0" width="130" height="12" fill="var(--grey)"/>
      <rect x="0" y="155" width="80" height="92" fill="var(--charcoal)"/>
      <rect x="0" y="252" width="140" height="78" fill="var(--blue)"/>
      <circle cx="180" cy="190" r="138" fill="var(--paper)"/>
    </svg>
    <div class="mark lg" style="left:100px;top:170px"><span class="dot"></span>KERNEL</div>
  </section>

  <!-- Open folder with letter -->
  <section class="item folder-open" style="left:683px;top:38px;width:480px;height:330px">
    <div style="position:absolute;left:240px;top:0;width:1px;height:100%;background:#e4e4e4"></div>
    <div class="item letter" style="left:250px;top:8px;width:185px;height:312px">
      <svg class="art" viewBox="0 0 185 312" aria-hidden="true">
        <polygon points="0,0 16,0 10,120 0,140" fill="var(--yellow)"/>
        <polygon points="40,0 185,0 185,10 60,12" fill="var(--charcoal)"/>
      </svg>
      <div class="mark xs" style="left:25px;top:28px"><span class="dot"></span>KERNEL</div>
      <div class="contact" style="left:120px;top:26px">Tower Nine, Level 12, Harbor Road, Lakeview<br>+000 4 555 0100<br>hello@kernelacademy.org<br>www.kernelacademy.org</div>
      <div class="fine" style="left:25px;top:85px;width:150px">
        <p><span class="to">Mr. John Doe</span><br>Managing Director,</p>
        <p>We are glad to welcome you to our next founders program. Our team will guide you through planning, funding and launch, step by step, with mentors who have built companies of their own.</p>
        <p>We are glad to welcome you to our next founders program. Our team will guide you through planning, funding and launch, step by step, with mentors who have built companies of their own.</p>
        <p>Best regards,</p>
      </div>
      <div class="sign" style="right:10px;top:250px">Chief Executive Officer<em>O. Rashed</em></div>
    </div>
  </section>

  <!-- Envelopes -->
  <section class="item envelope window" style="left:118px;top:415px;width:230px;height:110px">
    <svg class="art" viewBox="0 0 230 110" aria-hidden="true">
      <rect x="0" y="0" width="55" height="45" fill="var(--yellow)"/>
      <rect x="0" y="45" width="25" height="38" fill="var(--charcoal)"/>
      <rect x="0" y="85" width="45" height="25" fill="var(--blue)"/>
      <rect x="40" y="0" width="50" height="6" fill="var(--grey)"/>
      <ellipse cx="110" cy="45" rx="80" ry="50" fill="var(--paper)"/>
      <rect x="122" y="56" width="92" height="38" fill="none" stroke="#d4d4d4"/>
    </svg>
    <div class="mark xs" style="right:6px;top:6px"><span class="dot"></span>KERNEL</div>
  </section>

  <section class="item envelope back" style="left:385px;top:415px;width:230px;height:110px">
    <svg class="art" viewBox="0 0 230 110" aria-hidden="true">
      <rect x="0" y="0" width="230" height="22" fill="var(--grey)"/>
      <path d="M0 22 L60 22 C40 10 45 2 55 0 L230 0 L230 22Z" fill="var(--paper)" opacity=".0"/>
      <ellipse cx="150" cy="14" rx="100" ry="20" fill="var(--paper)"/>
    </svg>
    <div class="mark xs" style="right:8px;bottom:8px"><span class="dot"></span></div>
  </section>

  <section class="item envelope front" style="left:118px;top:550px;width:230px;height:110px">
    <svg class="art" viewBox="0 0 230 110" aria-hidden="true">
      <polygon points="0,0 230,0 230,4 20,12" fill="var(--yellow)"/>
      <polygon points="0,0 14,8 8,80 0,95" fill="var(--charcoal)"/>
    </svg>
    <div class="mark xs" style="left:165px;top:16px"><span class="dot"></span>KERNEL</div>
    <div class="contact" style="left:22px;top:62px">Tower Nine, Level 12, Harbor Road, Lakeview<br>+000 4 555 0100<br>hello@kernelacademy.org<br>www.kernelacademy.org</div>
  </section>

  <section class="item envelope flap" style="left:385px;top:550px;width:230px;height:110px">
    <svg class="art" viewBox="0 0 230 110" aria-hidden="true">
      <path d="M0 0 H230 V26 C150 30 80 34 0 42Z" fill="var(--yellow)"/>
    </svg>
    <div class="mark xs" style="right:8px;bottom:10px"><span class="dot"></span></div>
  </section>

  <!-- Markers left -->
  <div class="pen" style="left:42px;top:495px;width:14px;height:160px;background:var(--paper)">
    <div style="position:absolute;left:0;top:0;width:100%;height:38px;background:var(--blue);border-radius:6px 6px 0 0"></div>
    <div style="position:absolute;left:0;bottom:0;width:100%;height:12px;background:var(--blue);border-radius:0 0 6px 6px"></div>
    <span class="label">KERNEL</span>
  </div>
  <div class="pen" style="left:78px;top:495px;width:16px;height:165px;background:var(--paper)">
    <div style="position:absolute;left:0;top:0;width:100%;height:50px;background:var(--yellow);border-radius:6px 6px 0 0"></div>
    <div style="position:absolute;left:0;bottom:0;width:100%;height:14px;background:var(--yellow);border-radius:0 0 6px 6px"></div>
    <span class="label">KERNEL</span>
  </div>

  <!-- Letterhead with waves -->
  <section class="item letter wave" style="left:647px;top:408px;width:222px;height:310px">
    <svg class="art" viewBox="0 0 222 310" aria-hidden="true">
      <path d="M0 0 H222 V10 C150 20 80 4 0 16Z" fill="var(--blue)"/>
      <path d="M0 16 C80 4 150 20 222 10 V14 C150 26 80 10 0 22Z" fill="var(--yellow)"/>
      <path d="M0 300 C70 286 150 296 222 284 V310 H0Z" fill="var(--blue)"/>
      <path d="M0 296 C70 282 150 290 222 278 V284 C150 296 70 286 0 300Z" fill="var(--charcoal)"/>
    </svg>
    <div class="mark xs" style="left:10px;top:28px"><span class="dot"></span>KERNEL</div>
    <div class="contact" style="left:150px;top:30px;border-left:1px solid var(--blue);padding-left:4px">Tower Nine, Level 12, Harbor Road, Lakeview<br>+000 4 555 0100<br>hello@kernelacademy.org<br>www.kernelacademy.org</div>
    <div class="fine" style="left:10px;top:112px;width:34px;color:var(--blue)">Subject<br><span style="color:var(--ink)">Program Intake</span><br><br>Date<br><span style="color:var(--ink)">10/03/2024</span><br><br>Addressed to<br><span style="color:var(--ink)">John Doe</span></div>
    <div class="fine" style="left:38px;top:105px;width:170px">
      <p><span class="to">Mr. John Doe</span><br>Managing Director,</p>
      <p>We are glad to welcome you to our next founders program. Our team will guide you through planning, funding and launch, step by step, with mentors who have built companies of their own.</p>
      <p>We are glad to welcome you to our next founders program. Our team will guide you through planning, funding and launch, step by step, with mentors who have built companies of their own.</p>
      <p>Best regards,</p>
    </div>
    <div class="sign" style="right:12px;top:238px">Chief Executive Officer<em>O. Rashed</em></div>
  </section>

  <!-- Letterhead angled -->
  <section class="item letter angled" style="left:898px;top:408px;width:222px;height:310px">
    <svg class="art" viewBox="0 0 222 310" aria-hidden="true">
      <polygon points="0,0 18,0 12,130 0,150" fill="var(--yellow)"/>
      <polygon points="40,0 222,0 222,12 60,14" fill="var(--charcoal)"/>
    </svg>
    <div class="mark xs" style="left:30px;top:30px"><span class="dot"></span>KERNEL</div>
    <div class="contact" style="left:130px;top:26px">Tower Nine, Level 12, Harbor Road, Lakeview<br>+000 4 555 0100<br>hello@kernelacademy.org<br>www.kernelacademy.org</div>
    <div class="fine" style="left:35px;top:80px;width:175px">
      <p><span class="to">Mr. John Doe</span><br>Managing Director,</p>
      <p>We are glad to welcome you to our next founders program. Our team will guide you through planning, funding and launch, step by step, with mentors who have built companies of their own.</p>
      <p>We are glad to welcome you to our next founders program. Our team will guide you through planning, funding and launch, step by step, with mentors who have built companies of their own.</p>
      <p>Best regards,</p>
    </div>
  </section>

  <!-- Badges -->
  <div class="badge" style="left:1142px;top:542px;background:var(--blue)"><span></span></div>
  <div class="badge" style="left:1142px;top:590px;background:var(--charcoal)"><span></span></div>
  <div class="badge" style="left:1142px;top:638px;background:var(--yellow)"><span></span></div>

  <!-- Disc -->
  <section class="disc" style="position:absolute;left:35px;top:718px;width:160px;height:160px;border-radius:50%;background:var(--paper);box-shadow:0 2px 6px rgba(0,0,0,.15);overflow:hidden">
    <svg class="art" viewBox="0 0 160 160" style="position:absolute;inset:0" aria-hidden="true">
      <path d="M0 110 C40 108 70 130 85 160 L60 160 C50 140 25 128 0 128Z" fill="var(--yellow)"/>
      <path d="M160 108 C120 110 100 135 92 160 L118 160 C126 140 140 130 160 128Z" fill="var(--blue)"/>
      <circle cx="80" cy="80" r="24" fill="#e8e8ea" stroke="#d0d0d2"/>
      <circle cx="80" cy="80" r="9" fill="var(--bg)"/>
    </svg>
    <div class="mark xs" style="left:58px;top:18px"><span class="dot"></span>KERNEL</div>
  </section>

  <!-- Note pad -->
  <section class="item notepad" style="left:210px;top:727px;width:130px;height:135px">
    <svg class="art" viewBox="0 0 130 135" aria-hidden="true">
      <path d="M0 100 C40 112 90 112 130 100 V135 H0Z" fill="var(--yellow)"/>
    </svg>
    <div role="img" aria-label="Decorative pattern band" style="position:absolute;left:0;bottom:0;width:100%;height:20px;background:linear-gradient(var(--charcoal),#6a6a6d)"></div>
    <div class="mark xs" style="right:8px;top:6px"><span class="dot"></span>KERNEL</div>
  </section>

  <!-- Spiral notebook -->
  <section class="item notebook" style="left:405px;top:692px;width:185px;height:278px">
    <div style="position:absolute;left:0;top:0;width:100%;height:6px;background:repeating-linear-gradient(90deg,var(--charcoal) 0 3px,transparent 3px 6px)"></div>
    <svg class="art" viewBox="0 0 185 278" aria-hidden="true">
      <path d="M0 240 C60 232 125 232 185 240 V278 H0Z" fill="var(--yellow)"/>
    </svg>
    <div role="img" aria-label="Decorative pattern band" style="position:absolute;left:0;bottom:0;width:100%;height:22px;background:linear-gradient(var(--charcoal),#6a6a6d)"></div>
    <div class="mark xs" style="right:8px;top:14px"><span class="dot"></span>KERNEL</div>
    <div class="contact" style="left:0;width:100%;top:224px;text-align:center">Tower Nine, Level 12, Harbor Road, Lakeview<br>+000 4 555 0100 · hello@kernelacademy.org · www.kernelacademy.org</div>
  </section>

  <!-- Business cards -->
  <section class="item card" style="left:652px;top:818px;width:108px;height:50px">
    <svg class="art" viewBox="0 0 108 50" aria-hidden="true">
      <path d="M0 0 H108 V6 C70 12 30 2 0 10Z" fill="var(--blue)"/>
      <path d="M0 10 C30 2 70 12 108 6 V9 C70 15 30 5 0 13Z" fill="var(--yellow)"/>
    </svg>
    <div class="mark xs" style="left:20px;top:22px"><span class="dot"></span>KERNEL</div>
  </section>

  <section class="item card" style="left:767px;top:818px;width:105px;height:50px">
    <svg class="art" viewBox="0 0 105 50" aria-hidden="true">
      <path d="M0 0 H105 V16 C70 20 40 10 0 14Z" fill="var(--blue)"/>
      <path d="M80 50 L105 30 V50Z" fill="var(--charcoal)"/>
      <path d="M70 50 L105 24 V28 L76 50Z" fill="var(--yellow)"/>
    </svg>
    <div class="card-name" style="right:6px;top:2px">Omar Rashed</div>
    <div class="card-role" style="right:6px;top:9px">Chief Executive Officer</div>
    <div class="contact" style="left:6px;top:24px">Tower Nine, Level 12, Harbor Road, Lakeview<br>+000 4 555 0100<br>hello@kernelacademy.org<br>www.kernelacademy.org</div>
  </section>

  <section class="item card" style="left:900px;top:825px;width:68px;height:60px;background:var(--charcoal)">
    <svg class="art" viewBox="0 0 68 60" aria-hidden="true">
      <rect x="0" y="0" width="68" height="6" fill="var(--yellow)"/>
      <path d="M0 45 C25 38 45 42 68 36 V60 H0Z" fill="var(--blue)"/>
      <path d="M0 42 C25 35 45 39 68 33 V36 C45 42 25 38 0 45Z" fill="var(--yellow)"/>
      <ellipse cx="40" cy="22" rx="32" ry="14" fill="var(--paper)"/>
    </svg>
    <div class="mark xs" style="left:18px;top:18px"><span class="dot"></span>KERNEL</div>
  </section>

  <section class="item card" style="left:975px;top:825px;width:68px;height:60px;background:var(--charcoal)">
    <div class="card-name" style="left:6px;top:6px">Omar Rashed</div>
    <div class="card-role" style="left:6px;top:13px">Chief Executive Officer</div>
    <div class="contact" style="left:6px;top:22px;color:#d6d6d8">+000 4 555 0100<br>hello@kernelacademy.org<br>www.kernelacademy.org</div>
    <div style="position:absolute;left:0;bottom:0;width:100%;height:10px;background:var(--paper)"></div>
  </section>

  <!-- Ballpoint pens -->
  <div class="pen" style="left:1092px;top:770px;width:9px;height:140px;background:var(--blue)"><span class="label" style="color:var(--paper);font-size:6px">KERNEL</span></div>
  <div class="pen" style="left:1117px;top:770px;width:9px;height:140px;background:var(--charcoal)"><span class="label" style="color:var(--paper);font-size:6px">KERNEL</span></div>
  <div class="pen" style="left:1142px;top:770px;width:9px;height:140px;background:var(--yellow)"><span class="label" style="font-size:6px">KERNEL</span></div>

</main>
</body>
</html>
```